Business Card Design

I am a classical pilates instructor. I have a home studio, teach out a of a large studio downtown, and teach at on location corporate settings
I like my card to be very simple and clean.
I would like a silhouette of the picture I'm uploading on my design. In the upload section it looks like the picture is cut off and only showing a leg in the air...let me know if you can open up the entire picture.

Industry/Entity Type
Business
Contact Information for Business Card
Moira Kestley Pilates
Certified - The Pilates Center of Harnley
mo.kestley58@postvale.net
615.473.2186

```html
<!DOCTYPE html>
<html lang="en">
<head>
<meta charset="utf-8">
<title>Moira Kestley Pilates – Business Card</title>
<link rel="stylesheet" href="https://fonts.googleapis.com/css2?family=Poiret+One&family=Open+Sans:wght@400;600&display=swap">
<style>
  :root {
    --backdrop: #141414;
    --card-light: #e6e6e6;
    --card-light-edge: #b9b9b9;
    --card-dark: #121212;
    --card-dark-edge: #050505;
    --ink: #1a1a1a;
    --ink-soft: #3a3a3a;
    --rule-light: #d8d8d8;
    --silhouette: #111111;
  }
  * { margin: 0; padding: 0; box-sizing: border-box; }
  html, body {
    width: 1200px; height: 1134px; overflow: hidden;
    background: var(--backdrop);
  }
  .canvas {
    width: 1200px; height: 1134px;
    display: flex; flex-direction: column;
    align-items: center; justify-content: center; gap: 60px;
  }
  .card {
    width: 700px; height: 400px;
    position: relative; overflow: hidden;
    box-shadow: 0 18px 40px rgba(0,0,0,.6);
  }
  /* Front */
  .card-front {
    background: radial-gradient(ellipse at 55% 35%, #f6f6f6 0%, var(--card-light) 45%, var(--card-light-edge) 100%);
  }
  .silhouette {
    position: absolute; left: 40px; top: 40px;
    width: 220px; height: 330px;
    background: linear-gradient(180deg, #2a2a2a, var(--silhouette));
    border-radius: 110px 110px 30px 30px;
    opacity: .9;
  }
  .divider {
    position: absolute; left: 300px; top: 60px;
    width: 2px; height: 250px;
    background: linear-gradient(180deg, transparent, #ffffff 40%, #ffffff 60%, transparent);
    box-shadow: 3px 0 6px rgba(0,0,0,.25);
  }
  .details {
    position: absolute; left: 330px; top: 155px;
    color: var(--ink);
  }
  .details .name {
    font-family: "Poiret One", cursive;
    font-size: 34px; letter-spacing: 1px; line-height: 1;
  }
  .details .credential {
    font-family: "Open Sans", sans-serif;
    font-size: 22px; color: var(--ink-soft); margin-top: 6px;
  }
  .details .studio {
    font-family: "Open Sans", sans-serif;
    font-size: 14px; color: var(--ink-soft); margin-top: 2px;
  }
  .contact {
    list-style: none; margin-top: 18px;
    font-family: "Open Sans", sans-serif; font-size: 14px; color: var(--ink);
  }
  .contact li { display: flex; align-items: center; gap: 10px; margin-bottom: 6px; }
  .contact svg { width: 16px; height: 12px; fill: var(--ink); }
  /* Back */
  .card-back {
    background:
      repeating-linear-gradient(45deg, rgba(255,255,255,.015) 0 2px, transparent 2px 4px),
      radial-gradient(ellipse at 50% 40%, #262626 0%, var(--card-dark) 55%, var(--card-dark-edge) 100%);
  }
  .back-band {
    position: absolute; left: 0; right: 0; top: 165px; height: 70px;
    border-top: 1px solid var(--rule-light);
    border-bottom: 1px solid var(--rule-light);
    display: flex; align-items: center; justify-content: center;
  }
  .back-band .brand {
    font-family: "Poiret One", cursive;
    font-size: 38px; letter-spacing: 3px;
    color: #e8e8e8;
  }
</style>
</head>
<body>
<main class="canvas">
  <section class="card card-front">
    <div class="silhouette" role="img" aria-label="Black silhouette of a Pilates pose with legs raised overhead"></div>
    <div class="divider"></div>
    <div class="details">
      <h1 class="name">Moira Kestley</h1>
      <p class="credential">Pilates Certified</p>
      <p class="studio">The Pilates Center of Harnley</p>
      <ul class="contact">
        <li>
          <svg viewBox="0 0 16 12" aria-hidden="true"><path d="M0 0h16v12H0z M1 1.2v.6l7 5 7-5v-.6z" fill-rule="evenodd"/></svg>
          mo.kestley58@postvale.net
        </li>
        <li>
          <svg viewBox="0 0 16 12" aria-hidden="true"><path d="M1 3c0-2 2-3 7-3s7 1 7 3v1h-4V3H5v1H1z M3 5h10l1 7H2z"/></svg>
          615.473.2186
        </li>
      </ul>
    </div>
  </section>
  <section class="card card-back">
    <div class="back-band">
      <p class="brand">Moira Kestley Pilates</p>
    </div>
  </section>
</main>
</body>
</html>
```